Lumenfield Holdings

Professional looking business card using darker colours
I do not yet have a logo for the company so feel free to suggest
The business is based on consultancy and project management
Based in Melbourne
Business card can omit the word "Holdings" and can be Lumenfield consulting etc.

Business

Contact Name on card : Tom Verisco Contact number : +61412 305 617 Email address will be confirmed shortly.

```html
<!DOCTYPE html>
<html lang="en">
<head>
<meta charset="utf-8">
<title>Lumenfield Consulting – Business Card</title>
<link href="https://fonts.googleapis.com/css2?family=Montserrat:wght@600&family=Open+Sans:wght@400;600&display=swap" rel="stylesheet">
<style>
  :root {
    --backdrop: #3a3330;
    --card-dark: #1f1f21;
    --card-blue: #2a4f96;
    --accent-blue: #3a78d0;
    --text-light: #e8e8ea;
    --divider: #4a4a4e;
    --white: #ffffff;
  }
  * { margin: 0; padding: 0; box-sizing: border-box; }
  html, body { width: 1200px; height: 844px; overflow: hidden; }
  body {
    background: var(--backdrop);
    font-family: "Open Sans", sans-serif;
    position: relative;
  }
  .card {
    position: absolute;
    top: 272px;
    width: 525px;
    height: 300px;
    border-radius: 4px;
    box-shadow: 0 10px 28px rgba(0,0,0,0.45);
  }
  .card--back { left: 50px; background: var(--card-dark); }
  .card--front { left: 625px; background: var(--card-blue); }

  .brand {
    position: absolute;
    display: flex;
    flex-direction: column;
    align-items: center;
    text-align: center;
    font-family: "Montserrat", sans-serif;
    font-weight: 600;
    text-transform: uppercase;
  }
  .brand__dot {
    width: 34px; height: 34px; border-radius: 50%;
    margin-bottom: 12px;
  }
  .brand__name { font-size: 27px; letter-spacing: 1px; line-height: 1.15; }
  .brand__sub { font-size: 19px; letter-spacing: 8px; line-height: 1.4; }

  .card--back .brand { left: 36px; top: 100px; width: 270px; color: var(--accent-blue); }
  .card--back .brand__dot { background: var(--accent-blue); }
  .card--front .brand { left: 0; right: 0; top: 76px; color: var(--white); }
  .card--front .brand__dot { background: var(--white); }

  .card__divider {
    position: absolute; left: 312px; top: 44px; bottom: 44px;
    width: 1px; background: var(--divider);
  }
  .contact {
    position: absolute; left: 330px; top: 48px;
    color: var(--text-light); font-size: 13px; line-height: 1.35;
  }
  .contact__name { color: var(--accent-blue); font-size: 16px; font-weight: 600; }
  .contact__role { margin-bottom: 16px; }
  .contact__address { margin-bottom: 16px; }
  .contact__list { list-style: none; }
  .contact__list li { display: flex; align-items: center; gap: 8px; }
  .contact__list svg { width: 12px; height: 12px; flex: none; }
</style>
</head>
<body>
  <section class="card card--back" aria-label="Business card back">
    <div class="brand">
      <span class="brand__dot"></span>
      <span class="brand__name">Lumenfield</span>
      <span class="brand__sub">Consulting</span>
    </div>
    <div class="card__divider"></div>
    <div class="contact">
      <p class="contact__name">Tom Verisco</p>
      <p class="contact__role">Managing Director</p>
      <p class="contact__address">12345, Address Goes Here<br>Country Name, 123456.</p>
      <ul class="contact__list">
        <li>
          <svg viewBox="0 0 12 12" aria-hidden="true"><path fill="#3a78d0" d="M2.5 1h2l1 3-1.3 1a7 7 0 0 0 2.8 2.8L8 6.5l3 1v2c0 .8-.7 1.5-1.5 1.5A8.5 8.5 0 0 1 1 2.5C1 1.7 1.7 1 2.5 1z"/></svg>
          000-000 000 000
        </li>
        <li>
          <svg viewBox="0 0 12 12" aria-hidden="true"><rect x="0.5" y="2" width="11" height="8" fill="#3a78d0"/><path d="M0.5 2 6 6.5 11.5 2" fill="none" stroke="#1f1f21" stroke-width="1"/></svg>
          info@example.com
        </li>
        <li>
          <svg viewBox="0 0 12 12" aria-hidden="true"><path d="M5 7 7 5M4.5 5.5 3 7a1.8 1.8 0 0 0 2.5 2.5L7 8M7.5 6.5 9 5a1.8 1.8 0 0 0-2.5-2.5L5 4" fill="none" stroke="#3a78d0" stroke-width="1.4" stroke-linecap="round"/></svg>
          www.example.com
        </li>
      </ul>
    </div>
  </section>

  <section class="card card--front" aria-label="Business card front">
    <div class="brand">
      <span class="brand__dot"></span>
      <span class="brand__name">Lumenfield</span>
      <span class="brand__sub">Consulting</span>
    </div>
  </section>
</body>
</html>
```